Velmora Supply Company product labels (5"wide x7" high (12,5 cm x 17,5 cm))

We need a vertical product label that will go on the Gold stand up bags for our Kratom powder. We are looking for professional looking and attractive label design that will capture the attention of consumers. Our products should stand out when sitting on a shelf next to our competitors. We want one label which we will be able to use for all the different Kratom Powders we have.The product label will be used for several different varieties of Kratom so there will need to be an area available for the varieties name such as "RED BORNEO" or "GREEN MAENG DA" etc., which we will apply a small label as needed.
The label dimensions should be 5" wide x 7" high (12,5 cm wide x 17,5 cm high).
Please review the "must haves" section, and please try and include the "nice to haves" if possible.

Target Market(s)

Health minded consumers who love natural products, and are looking for plant based alternatives to harmful synthetic products.

Industry/Entity Type

Supplement

Colors

Designer to choose colors to be used in the design.

Requirements
Must have
• Product labels must include:
• 1) Company logo (find in the attachments)
• 2) Product information (find in the attachments)
• 3) Product title - Premium Kratom Powder
• 4) Weight indication - 250 grams
• 5) Barcode
• 6) Icon that says - 100% pure (or "100% natural")
Nice to have
• Indonesian jungle theme.
• Our packaging is gold metallic stand up bag, so the colors should be complimenting the bag.
Should not have
• labels or part of the labels taken from other Kratom companies. The design should be unique.

```html
<!DOCTYPE html>
<html lang="en">
<head>
<meta charset="utf-8">
<title>Velmora Supply Company – Premium Kratom Powder Label</title>
<link rel="stylesheet" href="https://fonts.googleapis.com/css2?family=Montserrat:wght@600;700;800&family=Open+Sans:wdth,wght@75..100,400..700&display=swap">
<style>
  :root {
    --page: #f2f2f0;
    --label-top: #ffffff;
    --label-sky: #bfe8f2;
    --forest: #4a5e3a;
    --forest-deep: #2f4a24;
    --gold: #c59a3e;
    --slate: #5f5f5f;
    --ink: #1c1c1c;
    --badge: #232323;
    --ribbon: #b59a72;
    --leaf-light: #d6e8bd;
    --leaf-mid: #9cc776;
    --jungle-a: #6aa444;
    --jungle-b: #2f6a26;
    --white: #ffffff;
  }
  * { box-sizing: border-box; margin: 0; padding: 0; }
  html, body { width: 1200px; height: 1000px; overflow: hidden; }
  body {
    background: var(--page);
    font-family: "Open Sans", Arial, sans-serif;
    position: relative;
  }
  .label {
    position: absolute;
    left: 280px; top: 52px;
    width: 640px; height: 896px;
    overflow: hidden;
    background: linear-gradient(180deg, var(--label-top) 0%, var(--label-top) 52%, var(--label-sky) 75%, var(--label-sky) 100%);
    box-shadow: 0 4px 18px rgba(0,0,0,0.15);
  }
  .foliage-top {
    position: absolute; left: 0; top: 0; width: 100%; height: 300px;
    background:
      radial-gradient(ellipse 150px 200px at 8% 30%, var(--leaf-mid) 0%, transparent 100%),
      radial-gradient(ellipse 150px 220px at 94% 45%, var(--leaf-mid) 0%, transparent 100%),
      radial-gradient(ellipse 320px 60px at 50% 0%, var(--leaf-light) 0%, transparent 100%);
    opacity: 0.85;
  }
  .jungle-bottom {
    position: absolute; left: 0; top: 540px; width: 100%; height: 356px;
    background:
      radial-gradient(ellipse 170px 320px at 100% 60%, var(--jungle-b) 0%, var(--jungle-a) 50%, transparent 100%),
      radial-gradient(ellipse 150px 300px at 0% 75%, var(--jungle-b) 0%, var(--jungle-a) 50%, transparent 100%),
      linear-gradient(180deg, rgba(106,164,68,0) 0%, rgba(106,164,68,0) 50%, var(--jungle-a) 75%, var(--jungle-b) 100%);
  }
  .brand {
    position: absolute; left: 0; top: 112px; width: 100%;
    display: flex; flex-direction: column; align-items: center; gap: 12px;
  }
  .brand-dot {
    width: 50px; height: 50px; border-radius: 50%;
    background: var(--forest-deep);
  }
  .brand-name {
    font-family: "Montserrat", Arial, sans-serif;
    font-weight: 700; font-size: 22px; letter-spacing: 1px;
    color: var(--forest-deep); text-transform: uppercase;
  }
  .title {
    position: absolute; left: 0; top: 288px; width: 100%;
    text-align: center;
    font-family: "Montserrat", Arial, sans-serif; font-weight: 800;
    line-height: 1;
  }
  .title-premium { display: block; color: var(--gold); font-size: 54px; }
  .title-kratom { display: block; color: var(--forest); font-size: 86px; margin-top: 6px; }
  .title-powder { display: block; color: var(--slate); font-size: 64px; margin-top: 6px; }
  .natural-badge {
    position: absolute; left: 30px; top: 488px; width: 128px; height: 128px;
  }
  .info {
    position: absolute; left: 186px; top: 553px; width: 250px;
    color: var(--ink);
    font-stretch: 75%;
  }
  .ingredients { font-weight: 700; font-size: 14px; line-height: 1.3; text-align: center; }
  .age-warning {
    margin-top: 12px; width: 248px;
    border: 2px solid var(--ink); padding: 4px 8px;
    font-weight: 700; font-size: 13px; line-height: 1.25; text-transform: uppercase;
    background: var(--white);
  }
  .disclaimer { margin-top: 16px; font-size: 13px; line-height: 1.22; text-align: justify; }
  .disclaimer strong { font-weight: 700; }
  .distributor {
    position: absolute; left: 46px; top: 842px;
    color: var(--white); font-size: 10px; line-height: 1.35; font-weight: 600;
  }
  .weight {
    position: absolute; left: 423px; top: 840px;
    color: var(--white); font-size: 25px; font-weight: 600;
  }
</style>
</head>
<body>
  <main class="label">
    <div class="foliage-top" role="img" aria-label="Hanging tropical leaves and vines along the top edge"></div>
    <div class="jungle-bottom" role="img" aria-label="Dense Indonesian jungle foliage with palm and banana leaves along the bottom"></div>

    <header class="brand">
      <span class="brand-dot"></span>
      <span class="brand-name">Velmora Supply Company</span>
    </header>

    <h1 class="title">
      <span class="title-premium">PREMIUM</span>
      <span class="title-kratom">KRATOM</span>
      <span class="title-powder">POWDER</span>
    </h1>

    <svg class="natural-badge" viewBox="0 0 128 128" aria-label="100% Natural">
      <circle cx="64" cy="58" r="56" fill="var(--badge)"/>
      <circle cx="64" cy="58" r="49" fill="none" stroke="var(--white)" stroke-width="1.5"/>
      <text x="64" y="66" text-anchor="middle" font-family="Montserrat, Arial, sans-serif" font-weight="800" font-size="28" fill="var(--white)">100%</text>
      <rect x="2" y="88" width="124" height="26" fill="var(--ribbon)"/>
      <text x="64" y="107" text-anchor="middle" font-family="Georgia, serif" font-weight="700" font-size="17" letter-spacing="2" fill="var(--white)">NATURAL</text>
    </svg>

    <section class="info">
      <p class="ingredients">Ingredients: 100% natural Mitragyna Speciosa leaf powder.</p>
      <p class="age-warning">Not for sale to minors. Must be 18 years or older to purchase. Keep out of reach of children.</p>
      <p class="disclaimer">Do not use any botanicals without a physician's consent, if you are a minor, pregnant, nursing or taking MAOIs. These statements have not been evaluated by the FDA and is not intended to diagnose, treat, cure or prevent any disease. <strong>Caution while driving or using heavy machinery.</strong></p>
    </section>

    <p class="distributor">Distributed by:<br>VELMORA SUPPLY COMPANY PINEMARSH, FL 32999</p>
    <p class="weight">Weight 250 g</p>
  </main>
</body>
</html>
```